Save planet earth it's the only planet with GIN

Tide Gin the brand is known for its Gin kits that are extremely popular; anyone can make their own Gin. The recipe is simple. Infuse non-flavoured alcohol with juniper and botanicals and produce your won gin in as little as 36 hours.
Now we are looking for a design or the embossing/printing of the label that will become the trademark for our first batch of Gin. This type of Gin methods is referred to as bathtub gin.
You can read more about is here

https://en.quorvapedia.example/wiki/Bathtub_gin

The Tide-Gin logo are currently on the packaging of the Gin Kits need to be incorporated in the design of the bottles.
We plan to launch a DRY GIN (also known as "no 8") and a Burnt Orange Gin (two designs). It is preferably that the bottles have a central theme. Although we have not yet makes a final decision about the bottle, we would like to suggest designing the label for the TRV ceramic 500ml bottle. The idea is presenting gin in ceramic that bathtubs are made off. (see pictures attached).

The design should contain all the elements you need on the label on a Gin bottle; visually it should cater for the elements of a craft product.

Colours should be fresh and taking into account the elements that are found in gin.

The first time I tasted gin, I immediately fell in love with the bitter taste of juniper, and although I did not realise it was the juniper berry that gave gin its distinct flavour. The smell of citrus zest, coriander seeds, cinnamon, cardamom, anise, pepper and liquorice, along with various flowers are some of the elements that we could include in the design.

The bottles will be white for the dry gin and Black for the Burnt Orange gin.

Reason: I am new on ArtFlockly and dont want the design to be rushed :)

Target Market(s)

Kings & Queens. Craft Gin Market. Cocktail bars.

Contact Information for Business Card

Logo in front detail in the back

John Doe
owner (or something funky)
number
email

Font styles to use
Other font styles liked:
• mercelle script regular & FV Almelo regular

Colors
f37122
0692cd
000000
ffffff
00a990

Requirements
Must have
• original logo

```html
<!DOCTYPE html>
<html lang="en">
<head>
<meta charset="utf-8">
<title>Tide-Gin Dry Gin Label</title>
<link rel="stylesheet" href="https://fonts.googleapis.com/css2?family=Pirata+One&family=Oswald:wght@400&display=swap">
<style>
  :root {
    --label-white: #ffffff;
    --ink-dark: #10262d;
    --ink-blue: #1d8fc0;
    --ink-line: #2a3a40;
    --berry-tone: #dfe6e8;
    --berry-tone-deep: #c9d3d6;
  }
  html, body {
    margin: 0;
    padding: 0;
    width: 1200px;
    height: 2380px;
    overflow: hidden;
    background: var(--label-white);
  }
  .label {
    position: relative;
    width: 1200px;
    height: 2380px;
    background: var(--label-white);
  }
  .label-frame {
    position: absolute;
    inset: 0;
    width: 1200px;
    height: 2380px;
  }
  .frame-line {
    fill: none;
    stroke: var(--ink-line);
    stroke-width: 7;
    stroke-linecap: round;
  }
  .rule {
    stroke: var(--ink-line);
    stroke-width: 4;
  }
  .dotted-arc {
    fill: none;
    stroke: var(--ink-dark);
    stroke-width: 12;
    stroke-linecap: round;
    stroke-dasharray: 0 26;
  }
  .side-dot { fill: var(--ink-dark); }
  .style-name {
    font-family: "Pirata One", serif;
    font-size: 120px;
    fill: var(--ink-dark);
  }
  .brand-name {
    font-family: "Pirata One", serif;
    font-size: 250px;
    fill: var(--ink-dark);
    letter-spacing: 2px;
  }
  .tagline {
    font-family: "Oswald", sans-serif;
    font-size: 48px;
    fill: var(--ink-blue);
    letter-spacing: 2px;
  }
  .curved-tagline {
    font-family: "Oswald", sans-serif;
    font-size: 64px;
    fill: var(--ink-blue);
    letter-spacing: 3px;
  }
  .strength {
    font-family: "Oswald", sans-serif;
    font-size: 52px;
    fill: var(--ink-dark);
  }
  .botanical-art {
    fill: url(#berryTone);
  }
</style>
</head>
<body>
<main class="label">
  <svg class="label-frame" viewBox="0 0 1200 2380" xmlns="http://www.w3.org/2000/svg">
    <defs>
      <radialGradient id="berryTone" cx="50%" cy="55%" r="60%">
        <stop offset="0%" stop-color="var(--berry-tone-deep)"/>
        <stop offset="100%" stop-color="var(--berry-tone)"/>
      </radialGradient>
      <path id="taglineCurve" d="M 170 1440 Q 600 1300 1040 1440"/>
    </defs>

    <!-- upper frame -->
    <path class="frame-line" d="M 110 680 L 110 150 Q 600 20 1090 150 L 1090 680"/>

    <text class="style-name" x="600" y="300" text-anchor="middle">Dry Gin</text>

    <path class="dotted-arc" d="M 230 575 Q 600 330 970 575"/>

    <text class="tagline" x="600" y="610" text-anchor="middle">BORN IN AFRICA</text>

    <line class="rule" x1="130" y1="745" x2="1070" y2="745"/>
    <line class="rule" x1="130" y1="773" x2="1070" y2="773"/>

    <text class="brand-name" x="600" y="1010" text-anchor="middle" textLength="1000" lengthAdjust="spacingAndGlyphs">Tide-Gin</text>

    <line class="rule" x1="130" y1="1137" x2="1070" y2="1137"/>
    <line class="rule" x1="130" y1="1165" x2="1070" y2="1165"/>

    <!-- lower frame -->
    <path class="frame-line" d="M 110 1190 L 110 2250 Q 600 2370 1090 2250 L 1090 1190"/>

    <text class="tagline" x="600" y="1240" text-anchor="middle">SINCE 2016</text>

    <text class="curved-tagline">
      <textPath href="#taglineCurve" startOffset="50%" text-anchor="middle">THE ORIGINAL BATHTUB GIN</textPath>
    </text>

    <circle class="side-dot" cx="215" cy="1710" r="11"/>
    <circle class="side-dot" cx="985" cy="1710" r="11"/>

    <ellipse class="botanical-art" cx="610" cy="1840" rx="320" ry="240" role="img" aria-label="Line drawing of a sprig of juniper berries with leaves"/>

    <text class="strength" x="600" y="2180" text-anchor="middle">43%VOL</text>
  </svg>
</main>
</body>
</html>
```